Ferris + Oakdale Architecture Ltd Stationary rebrand Lead designer to create a fresh clean modern...

We have recieved a great new logo design and now we are after a consistant fresh and modern stationary to match the new design. Business card design, Letter Head design, presentatnion folders and other stationery within the package. I have also added some of our existing layouts for presentation we would like updating with the new look, We would like a clean modern fresh design that looks visually pleasing on the page. we cant wait to see what you come up with!!!!

Target Market(s)

young professionals and middle age clients

Industry/Entity Type

Architect

Contact Information for Business Card

i have uploarded our orginal business card that has all the details attached.

Font styles to use
Sans Serif

Colors
000000
ffffff
d3d3d3

Requirements
Must have
• Logo and our contact information
Nice to have
• white sape around the card to give a clean look.

```html
<!DOCTYPE html>
<html lang="en">
<head>
<meta charset="utf-8">
<title>Ferris + Oakdale Architecture — Stationery</title>
<link rel="stylesheet" href="https://fonts.googleapis.com/css2?family=Lato:wght@400;700&display=swap">
<style>
  :root {
    --backdrop: #3a3a3c;
    --paper: #ffffff;
    --ink: #000000;
    --skyline-tone: #ededed;
    --skyline-tone-soft: #f7f7f7;
    --mark-grey: #d3d3d3;
  }
  * { margin: 0; padding: 0; box-sizing: border-box; }
  html, body { width: 1200px; height: 1200px; overflow: hidden; }
  body {
    background: var(--backdrop);
    font-family: "Lato", sans-serif;
    color: var(--ink);
    position: relative;
  }
  .skyline-art {
    position: absolute;
    background: linear-gradient(180deg, var(--skyline-tone-soft), var(--skyline-tone));
  }

  .letterhead {
    position: absolute;
    left: 64px; top: 56px;
    width: 610px; height: 791px;
    background: var(--paper);
    overflow: hidden;
  }
  .letterhead .skyline-left  { left: 12px;  top: 9px;  width: 253px; height: 71px; }
  .letterhead .skyline-right { left: 348px; top: 23px; width: 256px; height: 43px; }
  .corner-square {
    position: absolute; left: 0; top: 0; width: 100%; height: 100%;
  }
  .brand-square {
    position: absolute;
    background: var(--ink);
  }
  .letterhead .brand-square { left: 271px; top: 24px; width: 68px; height: 67px; }
  .brand-name {
    position: absolute;
    font-weight: 700;
    color: var(--ink);
    text-transform: uppercase;
    white-space: nowrap;
    line-height: 1;
  }
  .letterhead .brand-name {
    left: 0; width: 610px; top: 98px;
    text-align: center;
  }
  .brand-name .firm { display: block; font-size: 17px; letter-spacing: 0.06em; }
  .brand-name .discipline { display: block; font-size: 8px; letter-spacing: 0.62em; margin-top: 5px; padding-left: 0.62em; }
  .letterhead-footer {
    position: absolute;
    left: 25px; top: 757px;
    font-size: 13px;
    white-space: nowrap;
  }
  .letterhead-footer .phones { margin-left: 14px; }

  .business-card {
    position: absolute;
    left: 707px; top: 873px;
    width: 451px; height: 258px;
    background: var(--paper);
    overflow: hidden;
  }
  .business-card .skyline-art { left: 300px; top: 20px; width: 142px; height: 71px; }
  .business-card .brand-square { left: 14px; top: 14px; width: 69px; height: 68px; }
  .business-card .brand-name { left: 91px; top: 34px; }
  .business-card .brand-name .firm { font-size: 16px; letter-spacing: 0.05em; }
  .business-card .brand-name .discipline { font-size: 7.5px; letter-spacing: 0.7em; margin-top: 4px; padding-left: 0; }
  .holder {
    position: absolute;
    left: 0; width: 451px; top: 112px;
    text-align: center;
    text-transform: uppercase;
  }
  .holder-name { font-size: 19px; letter-spacing: 0.13em; }
  .holder-title { font-size: 11px; letter-spacing: 0.16em; margin-top: 2px; }
  .card-contact {
    position: absolute;
    left: 22px; top: 186px;
    font-size: 11.5px;
    line-height: 15.5px;
    list-style: none;
  }
</style>
</head>
<body>

<section class="letterhead" aria-label="Letterhead">
  <svg class="corner-square" viewBox="0 0 530 687" preserveAspectRatio="none" aria-hidden="true">
    <rect x="300" y="470" width="250" height="250" fill="none" stroke="var(--mark-grey)" stroke-width="22" transform="rotate(-30 425 595)"/>
  </svg>
  <div class="skyline-art skyline-left" role="img" aria-label="Line drawing of city tower skyline"></div>
  <div class="skyline-art skyline-right" role="img" aria-label="Line drawing of house rooflines"></div>
  <div class="brand-square"></div>
  <div class="brand-name">
    <span class="firm">Ferris + Oakdale</span>
    <span class="discipline">Architecture</span>
  </div>
  <p class="letterhead-footer">42 Kestrel Road Millbrook 7700 PO Box 3180 Millbrook 7740 <span class="phones">03 555 0142 &nbsp;/&nbsp; 0275 550 198</span></p>
</section>

<section class="business-card" aria-label="Business card">
  <div class="skyline-art" role="img" aria-label="Line drawing of skyline and house rooflines"></div>
  <div class="brand-square"></div>
  <div class="brand-name">
    <span class="firm">Ferris + Oakdale</span>
    <span class="discipline">Architecture</span>
  </div>
  <div class="holder">
    <p class="holder-name">Daniel Ferris</p>
    <p class="holder-title">Director</p>
  </div>
  <ul class="card-contact">
    <li>42 Kestrel Road Millbrook 7700 PO Box 3180 Millbrook 7740</li>
    <li>03 555 0142 &nbsp;/&nbsp; 0275 550 198</li>
    <li>daniel@foarchitecture.co.nz</li>
    <li>www.foarchitecture.co.nz</li>
  </ul>
</section>

</body>
</html>
```